We need our website look and feel updated to match our brand

We are looking to update our website and a "where to buy" tab at the top of the website. The current look and feel is ok but needs a clean up. The task is as follows:
1. Update the current pages and add a page for "Where to Buy"
2. Update the product page to reflect our current products. ie we have only three products now. Undercoat K, Undercoat M and GLAZEX. This page will have very similar descriptions and at the bottom of each product will be a link to our SDS (safety data sheets).
3. Please visit our current website for the look and feel.
4. Use our New Taglines need to be included. "Always Cleaning. All the Time." "24/7 SAFE SURFACE PROTECTION" (Logo as well)
5. The HomePage will need a nice clean location to our corporate video. https://clipvue.net/8kRtWmPzQaL (link for viewing) that will be the highlight and easy to access on the homepage.
Some examples of websites we like.
https://velmarix.com/
https://quorbelhall.com/ (like the use of motion graphics in these)
Our focus claims are that our product is a surface cleaner and deodorizer. We would like to see variations in black, white background (Black header bar) and Gray backgrounds.

```html
<!DOCTYPE html>
<html lang="en">
<head>
<meta charset="utf-8">
<title>Kelvane — Always Cleaning. All the Time.</title>
<link href="https://fonts.googleapis.com/css2?family=Poppins:wght@400;500;600;700&display=swap" rel="stylesheet">
<style>
:root{
  --yellow:#f6c415;
  --gold:#c8a313;
  --black:#000;
  --panel:#141414;
  --card:#1b1b1b;
  --white:#fff;
  --muted:#cfcfcf;
  --grey:#6b6b6b;
}
*{box-sizing:border-box;margin:0;padding:0}
html,body{width:1200px;height:5272px;overflow:hidden}
body{background:var(--black);color:var(--white);font-family:'Poppins',sans-serif;position:relative}
.abs{position:absolute}
.label{color:var(--yellow);font-size:13px;font-weight:600;text-transform:uppercase}
.h2{font-size:30px;font-weight:700;color:var(--white)}
.para{font-size:13px;line-height:23px;color:var(--muted)}
.more{color:var(--yellow);font-size:15px;font-weight:700;text-transform:uppercase;text-decoration:none}

/* header */
.site-header{left:0;top:0;width:1200px;height:143px;background:var(--black)}
.brand{left:90px;top:27px;display:flex;align-items:center;gap:14px}
.brand-box{width:40px;height:40px;border:5px solid var(--yellow)}
.brand-name{font-size:44px;font-weight:600;color:var(--white)}
.nav{left:336px;top:58px;display:flex;gap:36px;list-style:none}
.nav a{color:var(--white);font-size:14px;font-weight:600;text-decoration:none}
.nav .active{border-left:3px solid var(--yellow);border-top:3px solid var(--yellow);border-bottom:3px solid var(--yellow);padding:8px 6px;margin-top:-11px}

/* hero */
.hero{left:0;top:143px;width:1200px;height:619px;background:linear-gradient(90deg,#0c0c0c 0%,#2a2a2a 40%,#6e6e6e 75%,#9a9a9a 100%)}
.hero h1{left:113px;top:170px;font-size:64px;line-height:72px;font-weight:700}
.hero h1 span{color:var(--yellow);display:block}
.hero .tag{left:113px;top:330px;font-size:27px;font-weight:600}
.btn{background:var(--yellow);color:var(--black);font-weight:700;font-size:16px;text-transform:uppercase;display:flex;align-items:center;justify-content:center;text-decoration:none}
.hero .btn{left:113px;top:400px;width:158px;height:41px}

/* frames */
.frame{border:3px solid var(--yellow)}
.photo{background:linear-gradient(135deg,#cfd8e3,#6f86b5 55%,#2c3f7a)}

/* products */
.card{width:305px;height:465px;top:2700px;background:var(--card);text-align:center}
.card .img{position:absolute;left:62px;top:30px;width:181px;height:240px;background:linear-gradient(180deg,#f1f1f1,#b9b9b9)}
.card .img.gold{background:linear-gradient(180deg,#f7d23a,#d9a90c)}
.card h3{position:absolute;top:296px;width:100%;font-size:22px;font-weight:700}
.card p{position:absolute;top:334px;left:30px;width:245px;font-size:13px;line-height:24px;color:var(--muted)}
.card .price{position:absolute;top:389px;width:100%;font-size:16px;color:var(--yellow)}
.card .price s{margin-right:12px}
.card .stars{position:absolute;top:418px;width:100%;font-size:13px;color:var(--yellow);letter-spacing:1px}

/* faq & news */
.faq-item{left:113px;width:440px;border:1px solid #444;background:#0b0b0b;padding:16px 70px 12px 22px}
.faq-item h4{font-size:13px;font-weight:700;text-transform:uppercase;line-height:18px}
.faq-item p{font-size:12px;line-height:22px;color:#9a9a9a;margin-top:6px}
.faq-toggle{position:absolute;right:20px;top:14px;width:30px;height:30px;border-radius:50%;border:2px solid var(--yellow);color:var(--yellow);display:flex;align-items:center;justify-content:center;font-weight:700}
.news-img{width:152px;height:150px;background:linear-gradient(135deg,#bfd2ea,#3c5c93 60%,#1d2b4c)}
.news-text{width:330px}
.news-text h4{font-size:15px;font-weight:700}
.news-text .date{font-size:14px}
.news-text p{font-size:13px;line-height:23px;color:#9a9a9a;margin-top:6px}
.news-text a{color:var(--yellow);font-size:14px;font-weight:700;text-transform:uppercase;text-decoration:underline}

/* projects */
.project{top:4540px;width:266px;height:307px}
.project .img{width:266px;height:262px}
.project .tag{position:absolute;left:29px;bottom:0;width:208px;height:45px;background:var(--white);color:var(--black);font-size:14px;font-weight:700;text-transform:uppercase;display:flex;align-items:center;justify-content:center;border:2px solid #333}

/* footer */
.footer{left:0;top:4926px;width:1200px;height:286px;background:var(--gold)}
.footer h5{font-size:20px;font-weight:600;text-transform:uppercase}
.footer ul{list-style:none;margin-top:12px}
.footer li{font-size:13px;font-weight:600;text-transform:uppercase;line-height:29px}
.copyright{left:0;top:5212px;width:1200px;height:60px;background:var(--black);font-size:16px;display:flex;align-items:center;justify-content:center}
</style>
</head>
<body>

<header class="site-header abs">
  <div class="brand abs"><span class="brand-box"></span><span class="brand-name">Kelvane</span></div>
  <ul class="nav abs">
    <li><a class="active" href="#">Home</a></li>
    <li><a href="#">About Us</a></li>
    <li><a href="#">Where to Buy</a></li>
    <li><a href="#">Our Technology</a></li>
    <li><a href="#">News</a></li>
    <li><a href="#">FAQ</a></li>
    <li><a href="#">Contact</a></li>
  </ul>
</header>

<section class="hero abs" role="img" aria-label="Close-up photo of a periodic table of elements">
  <h1 class="abs">Always Cleaning.<span>All the Time.</span></h1>
  <div class="tag abs">24/7 Safe Surface Protection.</div>
  <a class="btn abs" href="#">Shop Now</a>
</section>

<!-- about -->
<div class="abs" style="left:129px;top:880px;width:496px;height:375px;border-top:3px solid var(--yellow);border-left:3px solid var(--yellow);border-bottom:3px solid var(--yellow)"></div>
<div class="abs" style="left:622px;top:880px;width:3px;height:20px;background:var(--yellow)"></div>
<div class="abs photo" style="left:180px;top:960px;width:330px;height:472px" role="img" aria-label="Gloved hand spraying cleaner from a blue spray bottle"></div>
<div class="abs label" style="left:569px;top:944px">About Us</div>
<div class="abs" style="left:569px;top:965px;font-size:30px;font-weight:700">Real World Solution</div>
<p class="abs para" style="left:569px;top:1018px;width:445px">The onset of COVID-19 has changed our lives forever. The current methods of cleaning surfaces are not sustainable. Cleaning the environment we live in with caustic UV-C light, ammonia-based cleaners and other harsh chemicals is wasteful. The moment you clean the surface and an infected person touches that surface again, it requires reapplication of your protective cleaners.</p>
<a class="abs more" style="left:569px;top:1174px" href="#">Read More</a>

<!-- technology -->
<div class="abs" style="left:588px;top:1491px;width:499px;height:377px;border-top:3px solid var(--yellow);border-right:3px solid var(--yellow);border-bottom:3px solid var(--yellow);clip-path:polygon(0 0,20% 0,20% 100%,0 100%,0 0,100% 0,100% 100%,0 100%)"></div>
<div class="abs" style="left:588px;top:1491px;width:3px;height:20px;background:var(--yellow)"></div>
<div class="abs" style="left:588px;top:1848px;width:3px;height:20px;background:var(--yellow)"></div>
<div class="abs" style="left:707px;top:1315px;width:328px;height:471px;background:linear-gradient(160deg,#e7f3ff,#7fc1ef 50%,#2a6fb3)" role="img" aria-label="Operating room in a hospital with surgical lights"></div>
<div class="abs label" style="left:130px;top:1543px;width:515px;text-align:right">How It Works</div>
<div class="abs" style="left:130px;top:1565px;width:515px;text-align:right;font-size:30px;font-weight:700">Kelvane Technology</div>
<p class="abs para" style="left:195px;top:1618px;width:450px;text-align:right">The onset of COVID-19 has changed our lives forever. The current methods of cleaning surfaces are not sustainable. Cleaning the environment, we live in with caustic UV-C light, ammonia-based cleaners and other harsh chemicals is wasteful. The moment you clean the surface and an infected person touches that surface again it requires reapplication of whatever you are using to keep the surfaces clean and safe.</p>
<a class="abs more" style="left:130px;top:1795px;width:515px;text-align:right" href="#">Read More</a>

<!-- video -->
<div class="abs" style="left:100px;top:1935px;width:1000px;height:568px;border:2px solid var(--yellow)"></div>
<a class="abs" href="https://clipvue.net/8kRtWmPzQaL" style="left:113px;top:1948px;width:975px;height:543px;background:linear-gradient(180deg,#d9ecf7 0%,#eef1f3 55%,#c8c8c8 100%)" role="img" aria-label="Corporate video: illustrated cleaning crew in protective suits spraying a café interior"></a>
<svg class="abs" style="left:1012px;top:2417px" width="54" height="54" viewBox="0 0 54 54"><circle cx="27" cy="27" r="24" fill="none" stroke="#e0352b" stroke-width="3"/><circle cx="27" cy="27" r="11" fill="none" stroke="#e0352b" stroke-width="2.5"/><path d="M24 22l8 5-8 5z" fill="#e0352b"/></svg>

<!-- products -->
<div class="abs label" style="left:0;top:2593px;width:1200px;text-align:center">Our Products</div>
<div class="abs" style="left:0;top:2616px;width:1200px;text-align:center;font-size:30px;font-weight:700">Kelvane Products</div>
<div class="abs card" style="left:115px">
  <div class="img" role="img" aria-label="White gallon jug of Undercoat K"></div>
  <h3>Undercoat K</h3>
  <p>Kelvane UV – Top Coat is applied on top of Kelvane UV – Binder.</p>
  <div class="price"><s>$ 45.00</s>$ 30.00</div>
  <div class="stars">★★★★☆</div>
</div>
<div class="abs card" style="left:449px">
  <div class="img gold" role="img" aria-label="Undercoat M jug with safety data sheet overlay"></div>
  <div style="position:absolute;left:85px;top:130px;width:135px;height:48px;background:#fff;color:#000;font-size:10px;font-weight:700;display:flex;align-items:center;justify-content:center;text-align:center;line-height:12px">VIEW SAFETY DATA<br>SHEETS</div>
  <h3>Undercoat M</h3>
  <p>Kelvane Visible Light is applied on top of Kelvane G -Binder.</p>
  <div class="price"><s>$ 45.00</s>$ 30.00</div>
  <div class="stars">★★★★☆</div>
</div>
<div class="abs card" style="left:782px">
  <div class="img" style="background:linear-gradient(180deg,#f4efd3,#d8c87a)" role="img" aria-label="Gallon jug of GLAZEX"></div>
  <h3>GLAZEX</h3>
  <p>Kelvane UV Binder Part A and B are combined in a 50/50 mix ratio.</p>
  <div class="price"><s>$ 45.00</s>$ 30.00</div>
  <div class="stars">★★★★☆</div>
</div>

<!-- newsletter -->
<div class="abs" style="left:0;top:3252px;width:1200px;height:486px;background:linear-gradient(90deg,#3a3005,#1a1a1a 30%,#1a1a1a 70%,#4a3c08)" role="img" aria-label="Product jugs on a dark background"></div>
<div class="abs" style="left:115px;top:3283px;width:448px;height:455px;border-top:3px solid var(--yellow);border-left:3px solid var(--yellow);border-bottom:3px solid var(--yellow)"></div>
<div class="abs" style="left:560px;top:3283px;width:3px;height:20px;background:var(--yellow)"></div>
<div class="abs" style="left:195px;top:3322px;width:657px;height:377px;background:var(--black)"></div>
<div class="abs label" style="left:244px;top:3402px">Signup</div>
<div class="abs" style="left:244px;top:3422px;font-size:30px;font-weight:700">Subscribe To Newsletter</div>
<p class="abs" style="left:244px;top:3476px;width:565px;font-size:12px;font-weight:600;line-height:23px">Kelvane has announced its plan to sell their unique Titanium Dioxide coatings in the United States. Kelvane is expanding its operations in these markets after using the materials in Japan for the past 25 years.</p>
<div class="abs" style="left:244px;top:3574px;width:336px;height:41px;background:#fff;color:#888;font-size:12px;padding:12px 20px">Email Address</div>
<a class="abs btn" style="left:580px;top:3574px;width:174px;height:41px;font-size:14px" href="#">Subscribe Now</a>

<!-- faq -->
<div class="abs label" style="left:113px;top:3846px">Frequently Asked Questions</div>
<div class="abs" style="left:113px;top:3866px;font-size:28px;font-weight:600">Latest FAQ’S</div>
<div class="abs faq-item" style="top:3928px;height:168px">
  <h4>How can you claim yout TiO2 coating is permanent?</h4>
  <p>As it generates hydroxyl radicals &amp; superoxides, it is clear that it oxidizes all bacteria, microorganisms and any organic particles. But it should subsequently also get reduced as well.</p>
  <span class="faq-toggle">+</span>
</div>
<div class="abs faq-item" style="top:4106px;height:51px">
  <h4>Does the TiO2 product have a shelf life?</h4>
  <span class="faq-toggle" style="top:10px">–</span>
</div>
<div class="abs faq-item" style="top:4168px;height:68px">
  <h4>Does the TiO2 product require mixing of other compounds?</h4>
  <span class="faq-toggle" style="top:18px">–</span>
</div>

<!-- news -->
<div class="abs label" style="left:598px;top:3846px">News</div>
<div class="abs" style="left:598px;top:3866px;font-size:28px;font-weight:600">Latest News</div>
<div class="abs news-img" style="left:598px;top:3922px" role="img" aria-label="Laboratory glassware in blue light"></div>
<div class="abs news-text" style="left:772px;top:3920px">
  <h4>News Title 1</h4><div class="date">08 Feb 2022</div>
  <p>Kelvane has announced its plan to sell their unique Titanium Dioxide coatings in the United States. Kelvane is expanding its</p>
  <a href="#">Read More</a>
</div>
<div class="abs news-img" style="left:598px;top:4086px;background:linear-gradient(135deg,#c9d6ee,#56688f 60%,#1d2336)" role="img" aria-label="Scientist working in a laboratory"></div>
<div class="abs news-text" style="left:772px;top:4084px">
  <h4>News Title 2</h4><div class="date">08 Feb 2022</div>
  <p>Kelvane has announced its plan to sell their unique Titanium Dioxide coatings in the United States. Kelvane is expanding its</p>
  <a href="#">Read More</a>
</div>

<!-- projects -->
<div class="abs label" style="left:0;top:4438px;width:1200px;text-align:center">Our Projects</div>
<div class="abs" style="left:0;top:4460px;width:1200px;text-align:center;font-size:30px;font-weight:700">Latest Projects</div>
<div class="abs project" style="left:37px"><div class="img" style="background:linear-gradient(160deg,#e3f2ff,#6cb3e6 55%,#24598f)" role="img" aria-label="Hospital operating room"></div><div class="tag">University Hospital</div></div>
<div class="abs project" style="left:324px"><div class="img" style="background:linear-gradient(160deg,#e9e9e9,#8c8c8c 55%,#3a3a3a)" role="img" aria-label="Restaurant building exterior in grey tones"></div><div class="tag">Burgerly Volcano</div></div>
<div class="abs project" style="left:610px"><div class="img" style="background:linear-gradient(160deg,#f4f4f4,#c4c4c4 55%,#7b7b7b)" role="img" aria-label="Clean public bathroom with stalls"></div><div class="tag">Odorless Bathrooms</div></div>
<div class="abs project" style="left:897px"><div class="img" style="background:linear-gradient(160deg,#d8a3a3,#9b3a3a 50%,#d9d9d9)" role="img" aria-label="Coated and non-coated test surfaces at a toll booth"></div><div class="tag">Toll Booth Test</div></div>

<!-- footer -->
<footer class="abs footer">
  <div class="abs" style="left:109px;top:65px;display:flex;align-items:center;gap:14px"><span style="width:36px;height:36px;border:5px solid #fff"></span><span style="font-size:50px;font-weight:600">Kelvane</span></div>
  <svg class="abs" style="left:142px;top:194px" width="160" height="30" viewBox="0 0 160 30">
    <circle cx="14" cy="15" r="13" fill="#fff"/><circle cx="57" cy="15" r="13" fill="#fff"/><circle cx="100" cy="15" r="13" fill="#fff"/><circle cx="143" cy="15" r="13" fill="#fff"/>
  </svg>
  <div class="abs" style="left:401px;top:62px"><h5>Quick Links</h5>
    <ul><li>Home</li><li>About Us</li><li>Wher to Buy</li><li>Latest News</li><li>Our Technology</li></ul></div>
  <div class="abs" style="left:625px;top:62px"><h5>Find Us</h5>
    <div style="margin-top:16px;display:flex;gap:14px;font-size:12px;line-height:20px">
      <svg width="16" height="20" viewBox="0 0 16 20"><path d="M8 0a7 7 0 0 0-7 7c0 5 7 13 7 13s7-8 7-13a7 7 0 0 0-7-7zm0 10a3 3 0 1 1 0-6 3 3 0 0 1 0 6z" fill="#fff"/></svg>
      <span>Kelvane,<br>Brookvale, RI USA</span></div>
    <div style="margin-top:12px;display:flex;gap:14px;font-size:12px">
      <svg width="16" height="16" viewBox="0 0 16 16"><path d="M3 1l3 3-2 2c1 2 3 4 5 5l2-2 3 3-2 3C6 15 1 10 0 3z" fill="#fff"/></svg>
      <span>+1 555 01 0199</span></div>
    <div style="margin-top:18px;display:flex;gap:14px;font-size:12px">
      <svg width="18" height="14" viewBox="0 0 18 14"><rect width="18" height="14" fill="#fff"/><path d="M1 1l8 7 8-7" stroke="#c8a313" stroke-width="1.6" fill="none"/></svg>
      <span>hello@kelvane.example</span></div>
  </div>
  <div class="abs" style="left:860px;top:62px"><h5>Sign Up</h5></div>
  <div class="abs" style="left:862px;top:112px;width:221px;height:41px;background:#fff;border-radius:4px;color:#555;font-size:13px;display:flex;align-items:center;justify-content:center">Email Address</div>
  <div class="abs" style="left:862px;top:169px;width:221px;height:41px;background:#fff;border-radius:4px;color:#000;font-size:13px;font-weight:700;display:flex;align-items:center;justify-content:center;gap:8px">SUBSCRIBE NOW <svg width="14" height="14" viewBox="0 0 14 14"><circle cx="7" cy="7" r="7" fill="#000"/><path d="M5 4l4 3-4 3z" fill="#fff"/></svg></div>
</footer>
<div class="abs copyright">Copyright © 2022 Kelvane. All Rights Reserved.</div>

</body>
</html>
```